Stationery (Business Cards, Letterheads & Envelopes)

Require stationery design which includes the following items as a minimum.

- Business card design
- Letterhead
- Envelopes

Details for business card:
Logo: Main logo is called "tovell interiors square gold" but you may make use of whichever logo works best.
Tagline: Exquisite Furniture & Furnishings
Name: Mirren Oskaby
Title: Interior Stylist
Mobile: 0427 318 942
PH: 03 9512 3470
Email: mirren@tovell-interiors.com.au

Industry/Entity Type

Business

```html
<!DOCTYPE html>
<html lang="en">
<head>
<meta charset="utf-8">
<title>Tovell Interiors Stationery</title>
<link rel="stylesheet" href="https://fonts.googleapis.com/css2?family=Cinzel:wght@500&family=Open+Sans:wght@400&display=swap">
<style>
  :root {
    --board: #e6e7ea;
    --ink: #050505;
    --card: #0d0d0d;
    --gold: #d9bd5a;
    --gold-light: #f1e07a;
    --band: #efe07c;
    --paper: #ffffff;
    --text: #222222;
    --window: #f7f7f7;
  }
  * { margin: 0; padding: 0; box-sizing: border-box; }
  html, body { width: 1200px; height: 1020px; overflow: hidden; }
  body { background: var(--board); position: relative; font-family: "Open Sans", Arial, sans-serif; }
  .piece { position: absolute; }

  .brand { display: flex; align-items: center; justify-content: center; gap: 10px;
    font-family: "Cinzel", Georgia, serif; font-weight: 500; color: var(--gold);
    white-space: nowrap; letter-spacing: 0.06em; }
  .brand-name { display: flex; flex-direction: column; align-items: center; line-height: 1.05; }
  .brand--stacked { flex-direction: column; }
  .brand-mark { border: 2px solid var(--gold); flex: none; }
  .brand--dark { color: var(--ink); }
  .brand--dark .brand-mark { border-color: var(--ink); }

  /* Presentation folder */
  .folder { left: 212px; top: 86px; width: 392px; height: 552px; background: var(--ink);
    display: flex; align-items: center; justify-content: center; }
  .folder .brand { font-size: 38px; gap: 14px; }
  .folder .brand-mark { width: 40px; height: 40px; }

  /* Letterhead */
  .letterhead { left: 654px; top: 88px; width: 391px; height: 554px; background: var(--paper);
    box-shadow: 0 0 2px rgba(0,0,0,.15); font-size: 10.5px; color: var(--text); }
  .letterhead-rule { position: absolute; top: 72px; height: 5px; width: 118px; background: var(--band); }
  .letterhead-rule--left { left: 7px; }
  .letterhead-rule--right { right: 7px; }
  .letterhead .brand { position: absolute; left: 125px; right: 125px; top: 12px; font-size: 16px; gap: 8px; }
  .letterhead .brand-mark { width: 22px; height: 22px; }
  .letter-date { position: absolute; right: 26px; top: 136px; }
  .letter-line { position: absolute; left: 48px; }
  .letter-close { position: absolute; right: 38px; top: 402px; width: 110px; text-align: center; line-height: 16px; }
  .signature { display: block; width: 60px; height: 30px; margin: 4px auto 4px;
    background: linear-gradient(90deg, #d8d8d8, #bdbdbd); border-radius: 3px; }
  .letter-footer { position: absolute; left: 0; right: 0; bottom: 0; height: 24px; background: var(--band);
    display: flex; align-items: center; justify-content: space-between; padding: 0 14px; font-size: 9.5px; }

  /* Envelope */
  .envelope { left: 62px; top: 664px; width: 404px; height: 251px; background: var(--ink); overflow: hidden; }
  .envelope-flap { position: absolute; inset: 0; }
  .envelope .brand { position: absolute; left: 14px; top: 78px; font-size: 24px; gap: 10px; }
  .envelope .brand-mark { width: 28px; height: 28px; }
  .envelope-window { position: absolute; left: 203px; top: 154px; width: 178px; height: 64px;
    background: var(--window); border-radius: 6px; }

  /* Business cards */
  .card { top: 704px; width: 324px; height: 186px; background: var(--card); color: var(--gold); }
  .card-front { left: 498px; text-align: center; }
  .card-front .brand { position: absolute; left: 0; right: 0; top: 12px; font-size: 20px; gap: 8px; }
  .card-front .brand-mark { width: 20px; height: 20px; }
  .card-edge { position: absolute; top: 22px; width: 12px; height: 140px; border-radius: 6px;
    background: linear-gradient(90deg, var(--gold), var(--gold-light)); }
  .card-edge--left { left: 0; border-radius: 0 6px 6px 0; }
  .card-edge--right { right: 0; border-radius: 6px 0 0 6px; }
  .card-divider { position: absolute; left: 38px; right: 47px; top: 121px; height: 2px; background: var(--gold); }
  .card-name { position: absolute; left: 0; right: 0; top: 139px; font-size: 12px; }
  .card-title { position: absolute; left: 0; right: 0; top: 157px; font-size: 10px; }

  .card-back { left: 848px; }
  .card-back .brand { position: absolute; left: 4px; width: 102px; top: 52px; font-size: 13px; gap: 6px; }
  .card-back .brand-mark { width: 14px; height: 14px; border-width: 1.5px; }
  .card-spine { position: absolute; left: 108px; top: 0; bottom: 0; width: 7px;
    background: linear-gradient(90deg, var(--gold), var(--gold-light)); }
  .card-tagline { position: absolute; left: 126px; top: 19px; font-size: 12px; }
  .card-back .card-name { left: 115px; top: 66px; text-align: center; }
  .card-back .card-title { left: 115px; top: 82px; text-align: center; }
  .contact-list { position: absolute; left: 130px; top: 122px; list-style: none; font-size: 9.5px; }
  .contact-list li { display: flex; align-items: center; gap: 8px; height: 17px; }
  .contact-list svg { width: 10px; height: 10px; fill: var(--gold); flex: none; }
</style>
</head>
<body>

  <section class="piece folder" aria-label="Presentation folder">
    <div class="brand"><span class="brand-mark"></span><span class="brand-name"><span>Tovell</span><span>Interiors</span></span></div>
  </section>

  <section class="piece letterhead" aria-label="Letterhead">
    <span class="letterhead-rule letterhead-rule--left"></span>
    <span class="letterhead-rule letterhead-rule--right"></span>
    <div class="brand brand--dark brand--stacked"><span class="brand-mark"></span><span class="brand-name"><span>Tovell</span><span>Interiors</span></span></div>
    <p class="letter-date">14 December 2014</p>
    <p class="letter-line" style="top:201px">[Insert Name and Address of Recipient]</p>
    <p class="letter-line" style="top:244px">Dear [Recipient's name]</p>
    <p class="letter-line" style="top:286px">[Insert subject line]</p>
    <p class="letter-line" style="top:328px">[Insert body of text]</p>
    <div class="letter-close">
      <p>Yours faithfully</p>
      <span class="signature" role="img" aria-label="Handwritten signature"></span>
      <p>Mirren Oskaby</p>
      <p>Interior Stylist</p>
    </div>
    <footer class="letter-footer">
      <span>PH: 03 9512 3470</span>
      <span>Mobile: 0427 318 942</span>
      <span>Email: mirren@tovell-interiors.com.au</span>
    </footer>
  </section>

  <section class="piece envelope" aria-label="Envelope">
    <svg class="envelope-flap" viewBox="0 0 404 251" aria-hidden="true">
      <polygon points="0,0 404,0 404,28 0,28" fill="#161616"/>
    </svg>
    <div class="brand"><span class="brand-mark"></span><span class="brand-name"><span>Tovell</span><span>Interiors</span></span></div>
    <span class="envelope-window"></span>
  </section>

  <section class="piece card card-front" aria-label="Business card front">
    <span class="card-edge card-edge--left"></span>
    <span class="card-edge card-edge--right"></span>
    <div class="brand brand--stacked"><span class="brand-mark"></span><span class="brand-name"><span>Tovell</span><span>Interiors</span></span></div>
    <span class="card-divider"></span>
    <p class="card-name">Mirren Oskaby</p>
    <p class="card-title">Interior Stylist</p>
  </section>

  <section class="piece card card-back" aria-label="Business card back">
    <div class="brand brand--stacked"><span class="brand-mark"></span><span class="brand-name"><span>Tovell</span><span>Interiors</span></span></div>
    <span class="card-spine"></span>
    <p class="card-tagline">Exquisite Furniture &amp; Furnishings</p>
    <p class="card-name">Mirren Oskaby</p>
    <p class="card-title">Interior Stylist</p>
    <ul class="contact-list">
      <li><svg viewBox="0 0 10 10" aria-hidden="true"><path d="M1 3 Q5 0 9 3 L8 4.5 L6.5 3.8 L6.5 3 H3.5 V3.8 L2 4.5 Z M2.5 5 H7.5 L8.5 9 H1.5 Z"/></svg>03 9512 3470</li>
      <li><svg viewBox="0 0 10 10" aria-hidden="true"><path d="M3 0.5 H7 V9.5 H3 Z M3.8 1.5 V7.5 H6.2 V1.5 Z"/></svg>0427 318 942</li>
      <li><svg viewBox="0 0 10 10" aria-hidden="true"><path d="M0.5 2 H9.5 V8 H0.5 Z M1.2 2.6 L5 5.6 L8.8 2.6 Z" fill-rule="evenodd"/></svg>mirren@tovell-interiors.com.au</li>
    </ul>
  </section>

</body>
</html>
```